Business Card - Cooperate

Business Card for Quorin Management Consulting

Target Market(s)

Corparte - b2B

Industry/Entity Type

Management Consulting - Professional Services

Contact Information for Business Card

Company Name , Slogan , Dummy Address,

Requirements
Must have
• Reach your Full Potential

```html
<!DOCTYPE html>
<html lang="en">
<head>
<meta charset="utf-8">
<title>Quorin Management Consulting – Business Card</title>
<link rel="stylesheet" href="https://fonts.googleapis.com/css2?family=Montserrat:wght@400;500;700&display=swap">
<style>
  :root {
    --page: #e9e9ec;
    --card: #1b1b1d;
    --brand-blue: #2e55cf;
    --name-green: #7ac143;
    --rule-blue: #2b2f8f;
    --text-light: #f2f2f2;
    --text-soft: #b9b9bf;
    --pattern-dark: #111113;
    --pattern-mid: #232326;
  }
  * { box-sizing: border-box; margin: 0; padding: 0; }
  html, body { width: 1200px; height: 912px; overflow: hidden; }
  body {
    background: var(--page);
    font-family: "Montserrat", sans-serif;
    position: relative;
  }
  .card {
    position: absolute;
    left: 285px;
    width: 630px;
    height: 360px;
    background: var(--card);
    border-radius: 4px;
    overflow: hidden;
    box-shadow: 0 10px 26px rgba(0,0,0,.25);
  }
  .card--front { top: 60px; }
  .card--back { top: 492px; }

  .emboss-pattern {
    position: absolute; inset: 0;
    background: linear-gradient(135deg, var(--pattern-dark) 0%, var(--pattern-mid) 55%, #2c2c30 100%);
  }

  .brand {
    position: absolute;
    display: flex;
    align-items: center;
    gap: 12px;
  }
  .brand__dot {
    width: 46px; height: 46px;
    border-radius: 50%;
    background: var(--brand-blue);
    flex: none;
  }
  .brand__name {
    font-weight: 500;
    font-size: 44px;
    line-height: 1;
    color: var(--brand-blue);
    letter-spacing: 1px;
  }
  .card--front .brand { left: 50%; top: 142px; transform: translateX(-50%); }
  .card--back .brand { right: 40px; top: 48px; }

  .slogan {
    position: absolute;
    font-weight: 400;
    font-size: 14px;
    color: var(--text-soft);
    white-space: nowrap;
  }
  .card--front .slogan { left: 0; right: 0; top: 206px; text-align: center; }
  .card--back .slogan { right: 40px; top: 118px; text-align: right; }

  .divider-long {
    position: absolute;
    left: 190px; right: 40px; top: 160px;
    height: 1.5px;
    background: var(--rule-blue);
  }
  .address {
    position: absolute;
    right: 40px; top: 184px;
    text-align: right;
    color: var(--text-light);
    font-size: 15px;
    font-style: normal;
    line-height: 1.4;
  }
  .person { position: absolute; left: 40px; top: 196px; }
  .person__name {
    font-weight: 700;
    font-size: 21px;
    color: var(--name-green);
    letter-spacing: .3px;
  }
  .person__role {
    font-size: 15px;
    color: var(--text-light);
    margin-top: 2px;
  }
  .divider-short {
    width: 150px; height: 1.5px;
    background: var(--rule-blue);
    margin: 9px 0;
  }
  .contacts { list-style: none; }
  .contacts li {
    display: flex; align-items: center; gap: 8px;
    color: var(--text-light);
    font-size: 15px;
    line-height: 1.45;
  }
  .contacts svg { width: 13px; height: 13px; flex: none; }
</style>
</head>
<body>
  <section class="card card--front">
    <div class="emboss-pattern" role="img" aria-label="Tone-on-tone embossed repeating pattern in dark grey"></div>
    <div class="brand">
      <span class="brand__dot"></span>
      <span class="brand__name">quorin</span>
    </div>
    <p class="slogan">Reach your full potential</p>
  </section>

  <section class="card card--back">
    <div class="brand">
      <span class="brand__dot"></span>
      <span class="brand__name">quorin</span>
    </div>
    <p class="slogan">Reach your full potential</p>
    <div class="divider-long"></div>
    <address class="address">
      1187 Larkspur Lane<br>Corvallis, OR 97330
    </address>
    <div class="person">
      <p class="person__name">DORIAN HALE</p>
      <p class="person__role">Director</p>
      <div class="divider-short"></div>
      <ul class="contacts">
        <li>
          <svg viewBox="0 0 16 16" aria-hidden="true"><path fill="#7ac143" d="M3.6 1.5l2.3 2.6-1.3 1.8c.9 2 2.5 3.6 4.5 4.5l1.8-1.3 2.6 2.3-1.2 2.2C7.4 15.4.6 8.6 1.4 2.7z"/></svg>
          (555) 218-4630
        </li>
        <li>
          <svg viewBox="0 0 16 16" aria-hidden="true"><rect x="1.5" y="3.5" width="13" height="9" fill="none" stroke="#7ac143" stroke-width="1.5"/><path d="M1.5 3.5L8 9l6.5-5.5" fill="none" stroke="#7ac143" stroke-width="1.5"/></svg>
          hello@quorinmail.com
        </li>
        <li>
          <svg viewBox="0 0 16 16" aria-hidden="true"><circle cx="8" cy="8" r="6.5" fill="none" stroke="#7ac143" stroke-width="1.4"/><ellipse cx="8" cy="8" rx="2.8" ry="6.5" fill="none" stroke="#7ac143" stroke-width="1.2"/><path d="M1.5 8h13M2.5 5h11M2.5 11h11" stroke="#7ac143" stroke-width="1.1"/></svg>
          www.quorinconsult.com
        </li>
      </ul>
    </div>
  </section>
</body>
</html>
```